business card for a massage therapy practice named 'Meadow and Willow Massage Studio'

I really need a trendy, yet easy on the eyes business card to complement my logo. Ideally with some gold or rose gold foil work.

My uploaded file of the logo I have in horizontal but I have a vertical version as well. Another color that is used in the website is a blush pink here and there. I'd like to see some trendy tropical leaves in the design.

```html
<!DOCTYPE html>
<html lang="en">
<head>
<meta charset="utf-8">
<title>Meadow and Willow Massage Studio – Business Card</title>
<link href="https://fonts.googleapis.com/css2?family=Roboto:wght@400;500;700&family=Allura&display=swap" rel="stylesheet">
<style>
  :root {
    --backdrop: #fbdde3;
    --card-white: #ffffff;
    --blush: #f1c8dd;
    --mint: #72cfa9;
    --mint-dark: #3fae86;
    --leaf-pink: #f3a9c6;
    --ink: #1d1d1f;
    --jungle-deep: #0f2a20;
    --jungle-mid: #1f5a3e;
    --jungle-light: #2f7a52;
    --jungle-berry: #7a3a4a;
  }
  * { margin: 0; padding: 0; box-sizing: border-box; }
  html, body {
    width: 1200px; height: 801px; overflow: hidden;
    background: var(--backdrop);
    font-family: "Roboto", Arial, sans-serif;
    color: var(--ink);
  }
  .card {
    position: absolute; top: 250px;
    width: 840px; height: 480px;
    transform: scale(0.625); transform-origin: top left;
    box-shadow: 0 10px 30px rgba(150, 90, 110, 0.22);
    overflow: hidden;
  }
  .card-front { left: 50px; background: var(--card-white); }
  .card-back { left: 625px; }

  /* Back */
  .leaf-pattern {
    position: absolute; inset: 0;
    background:
      radial-gradient(ellipse 45% 35% at 20% 25%, var(--jungle-light), transparent 70%),
      radial-gradient(ellipse 40% 40% at 80% 70%, var(--jungle-mid), transparent 70%),
      radial-gradient(ellipse 25% 20% at 60% 35%, var(--jungle-berry), transparent 70%),
      radial-gradient(ellipse 30% 25% at 30% 85%, var(--jungle-mid), transparent 70%),
      var(--jungle-deep);
  }
  .back-mark {
    position: absolute; left: 50%; top: 50%;
    transform: translate(-50%, -50%);
    display: flex; align-items: center; gap: 18px;
    font-weight: 500; font-size: 40px; color: var(--blush);
    white-space: nowrap;
  }
  .back-mark-dot {
    width: 22px; height: 22px; border-radius: 50%; background: var(--blush);
  }

  /* Front */
  .therapist { position: absolute; right: 56px; top: 40px; text-align: right; }
  .therapist-name { font-weight: 700; font-size: 22px; }
  .therapist-phone { font-size: 21px; margin-top: 2px; }

  .contact-band {
    position: absolute; left: 0; right: 0; top: 268px; bottom: 0;
    background: var(--blush);
  }

  .sessions-title {
    position: absolute; left: 52px; top: 128px;
    font-family: "Allura", cursive; font-weight: 400;
    font-size: 40px; color: var(--mint-dark);
  }
  .session-list {
    position: absolute; list-style: none; font-size: 19px; line-height: 27px;
  }
  .session-list li { display: flex; align-items: center; gap: 10px; white-space: nowrap; }
  .session-list.col-left { left: 64px; top: 176px; }
  .session-list.col-right { left: 492px; top: 176px; }
  .leaf-bullet { width: 12px; height: 12px; flex: none; }

  .studio { position: absolute; left: 66px; top: 296px; font-size: 20px; line-height: 27px; }
  .studio-name { font-weight: 700; font-size: 22px; }
  .studio-line { display: flex; align-items: center; gap: 14px; }
  .studio-line svg { width: 20px; height: 18px; flex: none; }

  .appointment {
    position: absolute; right: 60px; top: 300px; width: 250px;
    border: 4px solid var(--mint);
  }
  .appointment-label {
    background: var(--card-white); text-align: center;
    font-weight: 500; font-size: 17px; padding: 10px 0;
  }
  .appointment-phone {
    background: var(--mint); display: flex; align-items: center; justify-content: center;
    gap: 10px; font-weight: 700; font-size: 20px; padding: 10px 0;
  }
  .appointment-phone svg { width: 18px; height: 18px; }
</style>
</head>
<body>
<svg width="0" height="0" style="position:absolute">
  <defs>
    <symbol id="leaf" viewBox="0 0 12 12">
      <path d="M1 11 C1 4 5 1 11 1 C11 7 8 11 1 11 Z" fill="#f3a9c6"/>
      <path d="M1 11 L8 4" stroke="#ffffff" stroke-width="0.9"/>
    </symbol>
  </defs>
</svg>

<main class="card card-front">
  <div class="contact-band"></div>

  <header class="therapist">
    <p class="therapist-name">Marisol Vega</p>
    <p class="therapist-phone">713 555-0142</p>
  </header>

  <h2 class="sessions-title">Our Most Popular Sessions</h2>
  <ul class="session-list col-left">
    <li><svg class="leaf-bullet"><use href="#leaf"/></svg>Clinical Bodywork</li>
    <li><svg class="leaf-bullet"><use href="#leaf"/></svg>Therapeutic Massage</li>
    <li><svg class="leaf-bullet"><use href="#leaf"/></svg>Integrated Hot Stone Massage</li>
  </ul>
  <ul class="session-list col-right">
    <li><svg class="leaf-bullet"><use href="#leaf"/></svg>Lymphatic Drainage Massage</li>
    <li><svg class="leaf-bullet"><use href="#leaf"/></svg>Sacramento Sinus Facial</li>
    <li><svg class="leaf-bullet"><use href="#leaf"/></svg>Australian Foot Treatment</li>
  </ul>

  <section class="studio">
    <p class="studio-name">Meadow and Willow</p>
    <p>2180 Alder St. suite 210, Fairview, CA 95000</p>
    <p class="studio-line">
      <svg viewBox="0 0 20 18"><rect x="1" y="3" width="18" height="13" fill="#1d1d1f"/><path d="M1 3 L10 10 L19 3" stroke="#f1c8dd" stroke-width="1.6" fill="none"/></svg>
      meadowandwillow@mail.com
    </p>
    <p class="studio-line">
      <svg viewBox="0 0 20 18"><rect x="4" y="3" width="12" height="9" fill="none" stroke="#1d1d1f" stroke-width="1.6"/><path d="M1 15 H19" stroke="#1d1d1f" stroke-width="2"/></svg>
      www.meadowandwillow.com
    </p>
  </section>

  <aside class="appointment">
    <p class="appointment-label">Call for Appointment</p>
    <p class="appointment-phone">
      <svg viewBox="0 0 18 18"><path d="M4 1 L7 5 L5 7 C6 10 8 12 11 13 L13 11 L17 14 L15 17 C8 17 1 10 1 3 Z" fill="#1d1d1f"/></svg>
      (916) 555-0178
    </p>
  </aside>
</main>

<section class="card card-back">
  <div class="leaf-pattern" role="img" aria-label="Dark tropical leaf pattern with palm fronds, monstera leaves and a pink pineapple"></div>
  <p class="back-mark"><span class="back-mark-dot"></span>Meadow and Willow</p>
</section>
</body>
</html>
```